Tindle PR (young, fun PR agency) needs a Business Card Design

We need a new business card design that reflects who we are as a company. We're a Sydney-based PR agency that's six years old with clients including Blue Heron, Wavecrest, OVERA, Joe Calloway etc. - just check out our website for more info: www.tindlepr.com.au. We would like to see designs that bring to life our company name and what we do (generating media coverage for brands on TV, radio, online and in newspapers and magazines). We don't want a corporate style card but one that people take notice of and think 'wow that's a cool business card'. It doesn't have to be the standard rectangle shape and can incorporate humour.

Target Market(s)

Clients (generally cool/creative types) and media

Industry/Entity Type

Business

Requirements
Must have
• The card must feature our business logo (which can be updated if you like) and use both sides.
Nice to have
• The card could feature a cool illustration

```html
<!DOCTYPE html>
<html lang="en">
<head>
<meta charset="utf-8">
<title>Tindle PR – Business Card</title>
<link href="https://fonts.googleapis.com/css2?family=Archivo+Black&family=Roboto+Condensed:wght@700&family=Questrial&display=swap" rel="stylesheet">
<style>
  :root {
    --bg: #e9e6e1;
    --card: #ffffff;
    --ink: #1c1c1c;
    --orange: #f7a34c;
    --orange-text: #f39a3c;
    --shadow: rgba(0,0,0,0.18);
  }
  * { margin: 0; padding: 0; box-sizing: border-box; }
  html, body { width: 1200px; height: 900px; overflow: hidden; }
  body {
    background: var(--bg);
    font-family: "Questrial", sans-serif;
    color: var(--ink);
    position: relative;
  }
  .card {
    position: absolute;
    width: 540px;
    height: 330px;
    background: var(--card);
    box-shadow: 0 6px 18px var(--shadow);
    overflow: hidden;
  }
  .card-front { left: 40px; top: 285px; }
  .card-back  { left: 620px; top: 285px; }

  /* front */
  .front-band-top {
    position: absolute; left: 330px; top: 88px;
    width: 210px; height: 26px; background: var(--orange);
  }
  .front-logo {
    position: absolute; left: 34px; top: 128px;
    display: flex; align-items: center; gap: 14px;
  }
  .front-logo .brand-name {
    font-family: "Archivo Black", sans-serif;
    font-size: 54px; letter-spacing: 1px; line-height: 1;
    color: var(--ink);
  }
  .brand-dot {
    width: 34px; height: 34px; border-radius: 50%;
    background: var(--ink);
  }
  .front-band {
    position: absolute; left: 0; top: 196px;
    width: 330px; height: 34px; background: var(--orange);
    display: flex; align-items: center; padding-left: 36px;
  }
  .tagline {
    font-family: "Roboto Condensed", sans-serif; font-weight: 700;
    font-size: 22px; letter-spacing: 0.5px; color: var(--ink);
  }
  .front-web {
    position: absolute; right: 36px; top: 258px;
    font-size: 20px; letter-spacing: 0.5px; color: var(--orange-text);
  }

  /* back */
  .back-content { position: absolute; left: 250px; top: 48px; width: 260px; }
  .back-logo { display: flex; align-items: center; gap: 8px; }
  .back-logo .brand-name {
    font-family: "Archivo Black", sans-serif;
    font-size: 27px; line-height: 1; color: var(--ink);
  }
  .back-logo .brand-dot { width: 18px; height: 18px; }
  .back-band {
    margin-top: 3px; width: 190px; height: 15px; background: var(--orange);
    display: flex; align-items: center; padding-left: 6px;
  }
  .back-band .tagline { font-size: 11px; }
  .person-name { margin-top: 18px; font-size: 20px; color: var(--orange-text); }
  .person-role { font-size: 12px; margin-top: 2px; }
  .address { margin-top: 16px; font-size: 12px; line-height: 1.45; }
  .contacts { margin-top: 14px; list-style: none; font-size: 12px; line-height: 1.7; }
  .contacts li { display: flex; align-items: center; gap: 8px; }
  .contacts svg { width: 12px; height: 12px; flex: none; }
</style>
</head>
<body>

<section class="card card-front" aria-label="Card front">
  <div class="front-band-top"></div>
  <div class="front-logo">
    <span class="brand-name">TINDLE PR</span>
    <span class="brand-dot"></span>
  </div>
  <div class="front-band"><span class="tagline">PUBLIC RELATIONS</span></div>
  <p class="front-web">www.tindlepr.com.au</p>
</section>

<section class="card card-back" aria-label="Card back">
  <div class="back-content">
    <div class="back-logo">
      <span class="brand-name">TINDLE PR</span>
      <span class="brand-dot"></span>
    </div>
    <div class="back-band"><span class="tagline">PUBLIC RELATIONS</span></div>

    <p class="person-name">Clara Whitford</p>
    <p class="person-role">Managing Director</p>

    <p class="address">Level 2, 18 Bramble Street,<br>Surry Hills, Sydney 2010</p>

    <ul class="contacts">
      <li>
        <svg viewBox="0 0 12 12" aria-hidden="true"><path d="M2.5 1 L4.5 1 L5.2 3.5 L4 4.5 Q5 7 7.5 8 L8.5 6.8 L11 7.5 L11 9.5 Q10.5 11 9 11 Q1 10 1 2.8 Q1 1.2 2.5 1Z" fill="var(--orange)"/></svg>
        02 9000 4817
      </li>
      <li>
        <svg viewBox="0 0 12 12" aria-hidden="true"><rect x="0.8" y="2.5" width="10.4" height="7" fill="none" stroke="var(--orange)" stroke-width="1.2"/><path d="M0.8 2.5 L6 6.5 L11.2 2.5" fill="none" stroke="var(--orange)" stroke-width="1.2"/></svg>
        clara@tindlepr.com.au
      </li>
      <li>
        <svg viewBox="0 0 12 12" aria-hidden="true"><circle cx="6" cy="6" r="5" fill="none" stroke="var(--orange)" stroke-width="1.2"/><ellipse cx="6" cy="6" rx="2.2" ry="5" fill="none" stroke="var(--orange)" stroke-width="1"/><path d="M1 6 H11" stroke="var(--orange)" stroke-width="1"/></svg>
        www.tindlepr.com.au
      </li>
    </ul>
  </div>
</section>

</body>
</html>
```